WEB DESIGN AGENCY WEBSITE

the website is for "Web design and development company" VELNORA LTD.

I need a very clean, simple, professional design, it will be an ambassador for the company

1- I want one page design that begins with full screen image slider (4 images)
ex. (https://quillbarrow.com/)
2- images representation is the most important thing, so i need a 3 images sliders to be created that represents the below:
a. 1st image represents the company (WEB DESIGNING)
b. 2nd image represents (FULLY RESPONSIVE WEBSITES)
c. 3rd image represents (ECOMMERCE WEBSITES)
D. Social media integration
Please find the pictures I bought attached. Will send you the original files once the design is approved ( PLEASE FEEL FREE TO USE ANY OTHER PICS IF YOU FIND IT MORE CREATIVE )

it is very important that the 4 images have the same theme, very creative and presentable

3- the website must be responsive, and the mobile view is very very important, as more than 60% of web users access websites by phone or tablets (check quillbarrow website by phone)

4- the rest of the page will have the contents, please be creative this is a webdesign agency, need something WOW and professional and clean

website i like for the rest of the page:
https://www.dunmaretix.com/stylus
( i like the design, how the images are created, the colors, dark grey color in background everything)

again please make sure that all pictures used have excellent quality, creative and presentable, have the same theme

all information needed, about the contents you will find in this link:
http://velnoraltd.co.uk/VELNORAWEBSITE/HTML/index.html

please don't use any of the graphics elements, or the deign (we don't like it) it is just a template to display contents

you can change the logo color to white, if that will serve the design better, but of course it is much better to keep the logo color to keep the company identity

5- i need a contact us form at the end of the page

6- please create a portfolio part

many thanks for your time and efforts and good luck, please impress me :) whoever is the winner, will always have business with us

i have attached the logo and logo font

Requirements
Nice to have
• Dark grey back ground
Should not have
• no people pictures please
• i need specially made images like https://www.dunmaretix.com/stylus having same theme , look and feel, customized pics

```html
<!DOCTYPE html>
<html lang="en">
<head>
<meta charset="utf-8">
<title>VELNORA LTD — Web Design &amp; Development</title>
<link href="https://fonts.googleapis.com/css2?family=Raleway:wght@300;400;600;700;800&family=Open+Sans:wght@400;600&display=swap" rel="stylesheet">
<style>
:root{
  --bg:#3c3f45;
  --bg-deep:#303236;
  --accent:#1da0db;
  --text:#e6e8ea;
  --muted:#aeb3b8;
  --line:#5b5f66;
  --white:#ffffff;
}
*{margin:0;padding:0;box-sizing:border-box}
html,body{width:1200px;height:3822px;overflow:hidden}
body{background:var(--bg);color:var(--text);font-family:"Open Sans",Arial,sans-serif;position:relative}
.abs{position:absolute}
.heading{font-family:"Raleway",Arial,sans-serif;font-size:30px;letter-spacing:5px;font-weight:300;color:var(--text);text-align:center;width:100%}
.heading b{font-weight:800;color:var(--accent);border-left:2px solid var(--accent);padding-left:14px;margin-left:10px}
.center{left:0;width:1200px;text-align:center}

/* hero */
.hero{left:0;top:0;width:1200px;height:815px;
  background:
    radial-gradient(ellipse 420px 300px at 820px 250px,rgba(170,150,200,.75),transparent 70%),
    radial-gradient(ellipse 380px 260px at 1020px 480px,rgba(120,110,160,.7),transparent 70%),
    radial-gradient(ellipse 300px 220px at 700px 180px,rgba(225,228,238,.8),transparent 70%),
    radial-gradient(ellipse 520px 380px at 180px 620px,rgba(70,100,110,.75),transparent 70%),
    linear-gradient(100deg,#7f97a3 0%,#a7b7bf 28%,#8fa0b4 45%,#9a92b6 62%,#6d6a93 80%,#4b4f73 100%)}
.hero-shade{left:0;top:0;width:1200px;height:815px;background:linear-gradient(180deg,rgba(20,30,45,.1),rgba(20,30,45,.22))}
.brand{left:18px;top:18px;display:flex;align-items:center;gap:8px;font-family:"Raleway",sans-serif;font-weight:700;font-size:18px;letter-spacing:2px;color:var(--white)}
.brand i{width:22px;height:22px;background:var(--white);display:block}
.nav{right:90px;top:30px;display:flex;gap:14px;font-family:"Raleway",sans-serif;font-size:10px;letter-spacing:1px;color:var(--white);align-items:center}
.nav .active{border:1.5px solid var(--white);border-radius:14px;padding:4px 16px}
.nav a{padding:4px 8px}
.social-top{right:18px;top:30px;display:flex;gap:6px}
.social-top span,.follow span{width:20px;height:20px;border-radius:50%;background:rgba(255,255,255,.85);display:block}
.hero-title{top:350px;font-family:"Raleway",sans-serif;font-size:58px;letter-spacing:8px;font-weight:300;color:var(--white)}
.hero-title b{font-weight:800}
.hero-sub{top:424px;font-size:13px;letter-spacing:2px;color:var(--white);font-family:"Raleway",sans-serif;font-weight:600}
.slide-tab{top:370px;width:24px;height:84px;background:rgba(40,45,55,.7);color:var(--white);font-size:10px;letter-spacing:1px;display:flex;align-items:center;justify-content:center;writing-mode:vertical-rl}
.slide-tab.prev{left:0;border-radius:0 12px 12px 0}
.slide-tab.next{right:0;border-radius:12px 0 0 12px}

/* about */
.about-art{left:280px;top:853px;width:270px;height:205px;border-radius:8px;
  background:
    radial-gradient(circle at 30% 40%,rgba(150,155,165,.55),transparent 45%),
    radial-gradient(circle at 72% 62%,rgba(200,50,60,.55),transparent 35%),
    radial-gradient(circle at 80% 30%,rgba(230,190,60,.4),transparent 30%),
    linear-gradient(160deg,#4a4d54,#3e4147)}
.about-title{left:634px;top:870px;font-family:"Raleway",sans-serif;font-size:30px;letter-spacing:5px;font-weight:300}
.about-title b{font-weight:800;color:var(--accent);border-left:2px solid var(--accent);padding-left:14px;margin-left:6px}
.about-text{left:634px;top:928px;width:330px;font-size:11.5px;line-height:17px;color:var(--muted)}

/* services */
.services-title{top:1170px}
.services{left:158px;top:1256px;width:888px;display:grid;grid-template-columns:repeat(4,222px);grid-template-rows:148px 126px}
.service{text-align:center;padding-top:26px;border-right:1px solid var(--line);border-bottom:1px solid var(--line);font-family:"Raleway",sans-serif}
.service:nth-child(4n){border-right:none}
.service:nth-child(n+5){border-bottom:none;padding-top:22px}
.service svg{width:40px;height:34px;stroke:var(--white);fill:none;stroke-width:2}
.service h3{font-size:12.5px;font-weight:700;color:var(--white);margin-top:8px;letter-spacing:.5px}
.service p{font-size:9.5px;color:var(--muted);margin-top:3px;letter-spacing:.5px}
.service.featured{background:var(--accent)}
.service.featured p{color:var(--white);font-family:"Open Sans",sans-serif;font-size:10px;line-height:14px;padding:4px 22px 0}

/* process */
.process-title{top:1653px}
.process-text{top:1704px;font-size:11.5px;line-height:16px;color:var(--muted)}
.process-line{left:300px;top:1860px;width:602px;height:2px;background:var(--line)}
.step{top:1790px;width:160px;margin-left:-80px;text-align:center;font-family:"Raleway",sans-serif}
.step .ring{width:140px;height:140px;margin:0 auto;border-radius:50%;border:3px solid #2f5f78;background:var(--bg);display:flex;align-items:center;justify-content:center}
.step .disc{width:112px;height:112px;border-radius:50%;background:#e9ebee;display:flex;align-items:center;justify-content:center}
.step svg{width:52px;height:52px;fill:none;stroke:var(--accent);stroke-width:2.5}
.step h4{font-size:12.5px;font-weight:700;color:var(--white);margin-top:10px}
.step p{font-size:9.5px;color:var(--muted);margin-top:3px}

/* portfolio */
.portfolio-title{top:2028px}
.portfolio-text{top:2082px;font-size:11.5px;line-height:16px;color:var(--muted)}
.filters{top:2148px;display:flex;justify-content:center;gap:20px;font-size:10.5px;color:var(--muted);font-family:"Raleway",sans-serif}
.filters .active{border:1.5px solid var(--accent);color:var(--accent);border-radius:10px;padding:0 10px}
.tiles{left:0;top:2209px;width:1200px;display:grid;grid-template-columns:repeat(3,400px);grid-template-rows:400px 400px}
.tile{position:relative}
.tile-1{background:
  radial-gradient(circle at 50% 38%,rgba(70,160,150,.55),transparent 28%),
  radial-gradient(circle at 40% 45%,rgba(230,120,70,.45),transparent 30%),
  radial-gradient(ellipse 160px 50px at 50% 74%,rgba(240,225,200,.45),transparent 70%),
  linear-gradient(180deg,#4d4250,#463c49)}
.tile-2{background:
  radial-gradient(ellipse 170px 220px at 50% 48%,rgba(150,120,90,.55),transparent 70%),
  radial-gradient(circle at 50% 50%,#6b5440,#3a2e26 75%)}
.tile-3{background:
  radial-gradient(ellipse 95px 120px at 48% 35%,rgba(240,150,80,.75),transparent 70%),
  radial-gradient(ellipse 70px 90px at 42% 30%,rgba(120,90,180,.45),transparent 70%),
  radial-gradient(ellipse 90px 45px at 80% 55%,rgba(255,255,255,.8),transparent 70%),
  radial-gradient(ellipse 70px 35px at 22% 82%,rgba(255,255,255,.75),transparent 70%),
  linear-gradient(180deg,#b6d0f8,#a4c2f2)}
.tile-4{background:
  radial-gradient(ellipse 180px 75px at 45% 50%,rgba(245,220,80,.8),transparent 70%),
  radial-gradient(ellipse 60px 30px at 18% 15%,rgba(255,255,255,.75),transparent 70%),
  radial-gradient(ellipse 60px 30px at 28% 82%,rgba(255,255,255,.7),transparent 70%),
  linear-gradient(180deg,#f47474,#ec6262)}
.tile-5{background:
  radial-gradient(ellipse 130px 80px at 55% 55%,rgba(230,80,80,.55),transparent 70%),
  radial-gradient(ellipse 110px 60px at 58% 52%,rgba(240,240,245,.45),transparent 70%),
  radial-gradient(ellipse 50px 25px at 18% 58%,rgba(255,255,255,.55),transparent 70%),
  radial-gradient(circle at 50% 50%,#433d5e,#342f4b 75%)}
.tile-6{background:
  radial-gradient(ellipse 130px 70px at 50% 50%,rgba(30,25,25,.55),transparent 70%),
  radial-gradient(circle at 52% 62%,rgba(220,110,100,.5),transparent 20%),
  linear-gradient(180deg,#fcae86,#f99f74)}
.tile-hover{position:absolute;left:20px;top:20px;right:20px;bottom:20px;border:1px solid rgba(29,160,219,.7)}
.tile-actions{position:absolute;left:143px;top:180px;display:flex;gap:10px}
.tile-actions span{width:48px;height:48px;border-radius:50%;background:var(--accent);display:flex;align-items:center;justify-content:center}
.tile-actions svg{width:22px;height:22px;stroke:var(--white);fill:none;stroke-width:2.5}
.tile-label{position:absolute;left:60px;right:60px;top:280px;border-top:1px solid var(--accent);padding-top:10px;text-align:center;color:var(--accent);font-family:"Raleway",sans-serif;font-size:12px;letter-spacing:2px}

/* contact */
.contact-title{top:3062px}
.field{border:1px solid #8d9299;border-radius:3px;font-size:10px;letter-spacing:1px;color:#c9cdd1;padding:12px 10px 0;font-family:"Raleway",sans-serif}
.send{left:530px;top:3366px;width:140px;height:33px;border-radius:17px;background:var(--accent);color:var(--white);font-family:"Raleway",sans-serif;font-weight:700;font-size:10.5px;letter-spacing:1px;display:flex;align-items:center;justify-content:center}

/* footer */
.footer{left:0;top:3488px;width:1200px;height:334px;background:var(--bg-deep)}
.info{top:3448px;width:300px;margin-left:-150px;text-align:center}
.info .badge{width:80px;height:80px;border-radius:50%;background:var(--accent);margin:0 auto;display:flex;align-items:center;justify-content:center}
.info svg{width:26px;height:26px;fill:var(--white)}
.info h5{font-family:"Raleway",sans-serif;font-size:12.5px;letter-spacing:2px;color:var(--accent);font-weight:700;margin-top:16px}
.info p{font-size:12px;line-height:16px;color:var(--text);margin-top:12px}
.divider{left:255px;width:690px;height:1px;background:#474a50}
.follow-label{top:3674px;font-size:9.5px;letter-spacing:1px;color:var(--muted);font-family:"Raleway",sans-serif}
.follow{top:3708px;left:0;width:1200px;display:flex;justify-content:center;gap:12px}
.follow span{background:#e6e8ea}
.copyright{top:3786px;font-size:9px;letter-spacing:1px;color:var(--muted)}
</style>
</head>
<body>

<!-- hero -->
<div class="abs hero" role="img" aria-label="Close-up photograph of payment cards resting on a weathered blue wooden surface"></div>
<div class="abs hero-shade"></div>
<div class="abs brand"><i></i>VELNORA</div>
<nav class="abs nav"><span class="active">HOME</span><a>ABOUT US</a><a>SERVICES</a><a>PORTFOLIO</a><a>CONTACT</a></nav>
<div class="abs social-top"><span></span><span></span><span></span></div>
<div class="abs slide-tab prev">PREV</div>
<div class="abs slide-tab next">NEXT</div>
<h1 class="abs center hero-title">ECOMMERCE <b>WEBSITE</b></h1>
<p class="abs center hero-sub">WE DON'T JUST BUILD WEBSITES, WE BUILD YOUR BUSINESS</p>

<!-- about -->
<div class="abs about-art" role="img" aria-label="Isometric illustration of a laptop, phone, books, plant and desk items"></div>
<h2 class="abs about-title">WE ARE<b>CREATIVE</b></h2>
<p class="abs about-text">We are a creative web design agency. Our design experts offer the best balance of creativeness and user experience with their result oriented innovation and you get more than just a nice-looking design. We add value to your business and assist you in presenting a professional front to the marketplace through objective driven digital solutions by providing original creative designs to all types of businesses, small to corporate level.</p>

<!-- services -->
<h2 class="abs heading services-title">OUR<b>SERVICES</b></h2>
<div class="abs services">
  <div class="service"><svg viewBox="0 0 40 34"><rect x="4" y="4" width="32" height="22" rx="2"/><path d="M14 30h12M16 12l-4 3 4 3M24 12l4 3-4 3"/></svg><h3>WEB DESIGN</h3><p>WE ARE CREATIVE</p></div>
  <div class="service featured"><svg viewBox="0 0 40 34"><circle cx="16" cy="18" r="7"/><circle cx="28" cy="9" r="4"/><path d="M16 8v3M16 25v3M6 18h3M23 18h3"/></svg><h3>WEB DEVELOPMENT</h3><p>We ensure you of a vastly functional website that scores high in usability.</p></div>
  <div class="service"><svg viewBox="0 0 40 34"><path d="M6 4v26h30M10 24l8-9 6 5 10-12"/></svg><h3>ECOMMERCE DEVELOPMENT</h3><p>GENERATE MORE SALES</p></div>
  <div class="service"><svg viewBox="0 0 40 34"><rect x="4" y="5" width="28" height="22" rx="2"/><path d="M4 11h28"/><circle cx="31" cy="25" r="5"/></svg><h3>CMS DEVELOPMENT</h3><p>CONTENT MANAGEMENT SYSTEM</p></div>
  <div class="service"><svg viewBox="0 0 40 34"><rect x="3" y="6" width="22" height="16" rx="1"/><rect x="27" y="10" width="10" height="18" rx="2"/><path d="M10 28h10"/></svg><h3>RESPONSIVE WEBSITES</h3><p>OPTIMIZED FOR ALL DEVICES</p></div>
  <div class="service"><svg viewBox="0 0 40 34"><rect x="5" y="4" width="30" height="20" rx="2"/><circle cx="20" cy="14" r="5"/><path d="M14 30h12M20 24v6"/></svg><h3>ONLINE MARKETING</h3><p>SEO &amp; SEM SERVICES</p></div>
  <div class="service"><svg viewBox="0 0 40 34" style="fill:var(--white)"><circle cx="26" cy="8" r="5"/><circle cx="12" cy="18" r="5"/><circle cx="28" cy="26" r="5"/></svg><h3>SOCIAL MEDIA INTEGRATION</h3><p>MAKE YOUR BRAND SOCIALLY RELEVANT</p></div>
  <div class="service"><svg viewBox="0 0 40 34"><path d="M8 28L26 10M24 6l6 6M10 6l22 22M8 4l4 4"/></svg><h3>MAINTENANCE</h3><p>FREE SUPPORT</p></div>
</div>

<!-- process -->
<h2 class="abs heading process-title">WORK<b>PROCESS</b></h2>
<p class="abs center process-text">As a web design development company we build websites that perfectly captures owner's<br>imagination without compromising usability, marketability and functionality.</p>
<div class="abs process-line"></div>
<div class="abs step" style="left:300px"><div class="ring"><div class="disc"><svg viewBox="0 0 52 52"><rect x="12" y="8" width="28" height="36" rx="3"/><path d="M18 18h16M18 26h16M18 34h10"/></svg></div></div><h4>PLANNING</h4><p>ANALYSIS AND PLANNING</p></div>
<div class="abs step" style="left:502px"><div class="ring"><div class="disc"><svg viewBox="0 0 52 52"><rect x="6" y="10" width="40" height="26" rx="2"/><path d="M18 44h16M26 36v8M20 28l14-12"/></svg></div></div><h4>DESIGNING</h4><p>DESIGNING &amp; WIREFRAMING</p></div>
<div class="abs step" style="left:703px"><div class="ring"><div class="disc"><svg viewBox="0 0 52 52"><rect x="6" y="10" width="40" height="26" rx="2"/><circle cx="26" cy="23" r="7"/><path d="M18 44h16M26 36v8"/></svg></div></div><h4>DEVELOPMENT</h4><p>EXECUTION &amp; TESTING</p></div>
<div class="abs step" style="left:902px"><div class="ring"><div class="disc"><svg viewBox="0 0 52 52"><rect x="10" y="10" width="32" height="24" rx="2"/><path d="M4 40h44M26 16v12M21 21l5-5 5 5"/></svg></div></div><h4>LAUNCH</h4><p>LAUNCH &amp; SUPPORT</p></div>

<!-- portfolio -->
<h2 class="abs heading portfolio-title">OUR<b>PORTFOLIO</b></h2>
<p class="abs center portfolio-text">We Are Expert Web accusamus et iusto odio dignissimos ducimus qui blanditiis<br>praesentium voluptatum deleniti atque</p>
<div class="abs center filters"><span class="active">ALL</span><span>E-COMMERCE</span><span>SOCIAL SITES</span><span>MARKETPLACE</span></div>
<div class="abs tiles">
  <div class="tile tile-1" role="img" aria-label="Colourful hand-lettered doodle artwork on a dark purple background"></div>
  <div class="tile tile-2" role="img" aria-label="Sepia sketch illustration in a framed poster">
    <div class="tile-hover"></div>
    <div class="tile-actions">
      <span><svg viewBox="0 0 22 22"><circle cx="9" cy="9" r="6"/><path d="M14 14l6 6"/></svg></span>
      <span><svg viewBox="0 0 22 22"><rect x="3" y="8" width="9" height="6" rx="3"/><rect x="10" y="8" width="9" height="6" rx="3"/></svg></span>
    </div>
    <div class="tile-label">THE SOCIAL SITE</div>
  </div>
  <div class="tile tile-3" role="img" aria-label="Low-poly hot air balloon illustration among white clouds"></div>
  <div class="tile tile-4" role="img" aria-label="Low-poly yellow biplane illustration with clouds"></div>
  <div class="tile tile-5" role="img" aria-label="Flat rocket illustration flying among stars and clouds"></div>
  <div class="tile tile-6" role="img" aria-label="Flat novelty glasses and moustache illustration on peach"></div>
</div>

<!-- contact -->
<h2 class="abs heading contact-title">CONTACT<b>US</b></h2>
<div class="abs field" style="left:160px;top:3131px;width:431px;height:39px">FIRST NAME</div>
<div class="abs field" style="left:614px;top:3131px;width:426px;height:39px">LAST NAME</div>
<div class="abs field" style="left:160px;top:3192px;width:431px;height:39px">EMAIL ADDRESS</div>
<div class="abs field" style="left:614px;top:3192px;width:426px;height:39px">SUBJECT</div>
<div class="abs field" style="left:160px;top:3251px;width:880px;height:80px">MESSAGE</div>
<div class="abs send">SEND MESSAGE</div>

<!-- footer -->
<footer class="abs footer"></footer>
<div class="abs info" style="left:300px">
  <div class="badge"><svg viewBox="0 0 24 24"><path d="M6.6 10.8a15 15 0 006.6 6.6l2.2-2.2a1 1 0 011-.25 11.4 11.4 0 003.6.57 1 1 0 011 1V20a1 1 0 01-1 1A17 17 0 013 4a1 1 0 011-1h3.5a1 1 0 011 1c0 1.25.2 2.45.57 3.57a1 1 0 01-.25 1z"/></svg></div>
  <h5>CALL US AT</h5><p>+44-161-730-5528</p>
</div>
<div class="abs info" style="left:601px">
  <div class="badge"><svg viewBox="0 0 24 24"><path d="M3 6h18v12H3z" fill="none" stroke="#fff" stroke-width="2"/><path d="M3 6l9 7 9-7" fill="none" stroke="#fff" stroke-width="2"/></svg></div>
  <h5>MAIL US AT</h5><p>info@velnoraltd.co.uk</p>
</div>
<div class="abs info" style="left:900px">
  <div class="badge"><svg viewBox="0 0 24 24"><path d="M12 2a7 7 0 00-7 7c0 5 7 13 7 13s7-8 7-13a7 7 0 00-7-7zm0 9.5A2.5 2.5 0 1112 6.5a2.5 2.5 0 010 5z"/></svg></div>
  <h5>REACH US AT</h5><p>Harwick Enterprise Park<br>Meridian Centre 4<br>28 Calder Row, Harwick HW2 7QD</p>
</div>
<div class="abs divider" style="top:3643px"></div>
<p class="abs center follow-label">FOLLOW US AT</p>
<div class="abs follow"><span></span><span></span><span></span></div>
<div class="abs divider" style="top:3761px"></div>
<p class="abs center copyright">© VELNORA LTD. 2017</p>

</body>
</html>
```